Medical Clinic Group Looking for Website Design

We own and operate medical clinics and are looking looking to revamp our website. Our current website is www.marlowcarepartners.ca We need our website to be more functional, user friendly, and easier to maintain.

```html
<!DOCTYPE html>
<html lang="en">
<head>
<meta charset="utf-8">
<title>Marlow Care Partners</title>
<link rel="stylesheet" href="https://fonts.googleapis.com/css2?family=Jost:wght@300;400;500&display=swap">
<style>
:root{
  --teal:#3dd1dc;
  --ink:#6b6c6e;
  --ink-soft:#7d7e80;
  --button:#77787a;
  --line:#d9d9d9;
  --panel:#f0f0f0;
  --footer:#7a7a7b;
  --footer-bar:#6d6d6e;
  --white:#ffffff;
}
*{margin:0;padding:0;box-sizing:border-box}
html,body{width:1200px;height:2674px;overflow:hidden}
body{font-family:"Jost",sans-serif;color:var(--ink);background:var(--white);position:relative}
.abs{position:absolute}
a{color:inherit;text-decoration:none}

.site-header{position:absolute;left:0;top:0;width:1200px;height:75px;background:var(--white);box-shadow:0 1px 6px rgba(0,0,0,.05);z-index:2}
.brand{position:absolute;display:flex;align-items:center;gap:10px;font-weight:400;color:var(--teal);font-size:22px;letter-spacing:.5px}
.brand-dot{width:22px;height:22px;border-radius:50%;background:var(--teal)}
.main-nav{position:absolute;top:30px;left:508px;display:flex;gap:0;font-size:12px;color:var(--ink)}
.main-nav span{position:absolute;white-space:nowrap}
.btn{position:absolute;display:flex;align-items:center;justify-content:center;font-size:12px;font-weight:500;color:var(--white);border-radius:3px;background:var(--button)}
.btn.teal{background:var(--teal)}

.hero{position:absolute;left:0;top:75px;width:1200px;height:500px;background:linear-gradient(100deg,#f4f4f4 0%,#ececec 55%,#e4e4e4 100%)}
.eyebrow{position:absolute;color:var(--teal);font-size:15px;font-weight:400;letter-spacing:.3px}
.heading{position:absolute;font-size:30px;font-weight:400;line-height:36px;color:var(--ink)}
.body-copy{position:absolute;font-size:11.2px;line-height:18.7px;font-weight:300;color:var(--ink)}
.photo{position:absolute}

.quick-links{position:absolute;left:0;top:575px;width:1200px;height:400px}
.tile{position:absolute;width:270px;text-align:center;font-size:15.5px;font-weight:300;color:var(--ink)}
.tile svg{display:block;margin:0 auto 12px}

.sports{position:absolute;left:0;top:975px;width:1200px;height:445px;background:linear-gradient(90deg,#f3f6f9 0%,#fbfcfd 45%,#f2f6fa 100%)}
.online{position:absolute;left:0;top:1420px;width:1200px;height:437px;background:var(--panel)}
.renovate{position:absolute;left:0;top:1857px;width:1200px;height:438px;background:var(--white)}

.site-footer{position:absolute;left:0;top:2295px;width:1200px;height:341px;background:var(--footer);color:var(--white)}
.footer-title{position:absolute;font-size:16.5px;font-weight:400}
.footer-list{position:absolute;list-style:none;font-size:11.5px;font-weight:300;line-height:22.5px}
.footer-bar{position:absolute;left:0;top:2636px;width:1200px;height:38px;background:var(--footer-bar);color:var(--white);font-size:10px;font-weight:300;text-align:center;line-height:38px}
.footer-bar span{margin:0 14px}
</style>
</head>
<body>

<header class="site-header">
  <div class="brand" style="left:106px;top:24px"><span class="brand-dot"></span>Marlow Care Partners</div>
  <nav class="main-nav" aria-label="Main">
    <span style="left:0">Locations</span>
    <span style="left:84px">For Patients ⌄</span>
    <span style="left:191px">For Providers ⌄</span>
    <span style="left:306px">Careers</span>
    <span style="left:381px">About Us ⌄</span>
  </nav>
  <a class="btn teal" style="left:981px;top:19px;width:113px;height:37px">Book Online</a>
</header>

<section class="hero">
  <p class="eyebrow" style="left:106px;top:146px">Marlow Care Partners</p>
  <h1 class="heading" style="left:106px;top:168px">We simplify providing care</h1>
  <p class="body-copy" style="left:106px;top:215px;width:390px">Through our years of experience working with healthcare providers, we have developed customizable practice management solutions that are proven to substantially reduce practice overhead and administrative burden; increase provider and patient satisfaction; and remove the added pressure of managing a business and employees.</p>
  <a class="btn" style="left:106px;top:312px;width:113px;height:38px">About Us</a>
  <div class="photo" role="img" aria-label="Doctor using a laptop with digital health interface overlay" style="left:613px;top:113px;width:481px;height:274px;background:linear-gradient(120deg,#c9d7e2 0%,#e4e8ec 45%,#eadfd3 75%,#f3c9a0 100%)"></div>
</section>

<section class="quick-links">
  <svg class="abs" style="left:0;top:0" width="1200" height="400" aria-hidden="true">
    <line x1="463" y1="63" x2="463" y2="400" stroke="#d9d9d9"/>
    <line x1="738" y1="63" x2="738" y2="400" stroke="#d9d9d9"/>
    <line x1="200" y1="231" x2="1000" y2="231" stroke="#d9d9d9"/>
  </svg>
  <div class="tile" style="left:190px;top:102px">
    <svg width="56" height="46" viewBox="0 0 56 46" fill="none" stroke="#3dd1dc" stroke-width="2"><circle cx="22" cy="13" r="9"/><path d="M4 44c0-11 8-18 18-18s18 7 18 18"/><circle cx="37" cy="11" r="7"/><path d="M40 24c8 2 13 8 13 18"/></svg>
    Find a Provider
  </div>
  <div class="tile" style="left:465px;top:102px">
    <svg width="50" height="46" viewBox="0 0 50 46" fill="none" stroke="#3dd1dc" stroke-width="2"><path d="M25 43C8 31 3 22 3 14 3 7 9 2 15 2c5 0 8 3 10 6 2-3 5-6 10-6 6 0 12 5 12 12 0 8-5 17-22 29z"/><path d="M21 14h8v6h6v8h-6v6h-8v-6h-6v-8h6z"/></svg>
    Services
  </div>
  <div class="tile" style="left:740px;top:102px">
    <svg width="48" height="46" viewBox="0 0 48 46" fill="none" stroke="#3dd1dc" stroke-width="2"><rect x="3" y="6" width="40" height="36" rx="2"/><line x1="3" y1="15" x2="43" y2="15"/><line x1="12" y1="2" x2="12" y2="10"/><line x1="34" y1="2" x2="34" y2="10"/><path d="M10 22h26M10 29h26M10 36h18M17 18v22M26 18v22"/><circle cx="38" cy="38" r="6" fill="#fff"/><path d="M35 38l2 2 4-4"/></svg>
    Book an Appointment
  </div>
  <div class="tile" style="left:190px;top:284px">
    <svg width="46" height="46" viewBox="0 0 46 46" fill="none" stroke="#3dd1dc" stroke-width="2"><path d="M23 34C15 24 11 18 11 12a12 12 0 0124 0c0 6-4 12-12 22z"/><circle cx="23" cy="12" r="5"/><path d="M13 30L4 44h38l-9-14"/></svg>
    Locations
  </div>
  <div class="tile" style="left:465px;top:284px">
    <svg width="46" height="46" viewBox="0 0 46 46" fill="none" stroke="#3dd1dc" stroke-width="2"><rect x="4" y="10" width="34" height="24" rx="1"/><rect x="10" y="3" width="32" height="24" rx="1" fill="#fff"/><path d="M15 10h22M15 16h22M15 22h14M17 34v8M25 34v8M12 43h18"/></svg>
    Patient Resources
  </div>
  <div class="tile" style="left:740px;top:284px">
    <svg width="48" height="46" viewBox="0 0 48 46" fill="none" stroke="#3dd1dc" stroke-width="2"><path d="M6 4l8-1 5 10-5 4c3 7 8 12 15 15l4-5 10 5-1 8c-20 1-37-16-36-36z"/><rect x="24" y="4" width="20" height="14" rx="3"/><path d="M29 11h1M34 11h1M39 11h1"/></svg>
    Contact Us
  </div>
</section>

<section class="sports">
  <svg class="abs" style="left:180px;top:55px" width="400" height="330" aria-hidden="true">
    <polygon points="200,8 390,167 200,326 10,167" fill="none" stroke="#7c7d80" stroke-width="1.5" transform="translate(-2 0)"/>
    <polygon points="210,8 390,167 210,326" fill="none" stroke="#9a9b9d" stroke-width="1.5"/>
    <polygon points="180,8 340,167 180,326 20,167" fill="#d9c7b6" role="img" aria-label="Clinician examining a patient's knee"/>
  </svg>
  <p class="eyebrow" style="left:613px;top:89px">Your partner in health</p>
  <h2 class="heading" style="left:613px;top:111px;width:360px">Sports medicine services now available at our lakeshore location</h2>
  <p class="body-copy" style="left:613px;top:229px;width:380px">Marlow Care Partners is continually adding and improving our services to provide patients with access to comprehensive care under one roof. Speak with your healthcare provider about how interventional MSK treatments and regenerative therapy can help you today!</p>
  <a class="btn" style="left:613px;top:322px;width:181px;height:38px">Download Referral Form</a>
</section>

<section class="online">
  <p class="eyebrow" style="left:200px;top:83px">Easy access to care when you need it</p>
  <h2 class="heading" style="left:200px;top:105px;width:360px">Online appointment booking now available to all patients</h2>
  <p class="body-copy" style="left:200px;top:222px;width:385px">Marlow Care Partners continues to create options that better suit your lifestyle. Book your appointment when it's convenient for you, even if you don't have a family doctor.</p>
  <a class="btn" style="left:200px;top:315px;width:175px;height:38px">Book at Ridgeview Medical</a>
  <a class="btn teal" style="left:387px;top:315px;width:113px;height:38px">Locations</a>
  <svg class="abs" style="left:650px;top:25px" width="330" height="400" aria-hidden="true">
    <polygon points="165,100 320,250 165,375 10,250" fill="none" stroke="#9a9b9d" stroke-width="1.5"/>
    <polygon points="165,8 320,167 165,326 10,167" fill="#8a939c" role="img" aria-label="Hands typing on a laptop beside a coffee cup"/>
  </svg>
</section>

<section class="renovate">
  <svg class="abs" style="left:190px;top:25px" width="400" height="330" aria-hidden="true">
    <polygon points="185,4 20,165 185,326" fill="none" stroke="#9a9b9d" stroke-width="1.5"/>
    <polygon points="200,4 10,165 200,326" fill="none" stroke="#7c7d80" stroke-width="1.5"/>
    <polygon points="230,4 380,165 230,326 70,165" fill="#d7d3cd" role="img" aria-label="Smiling woman seated in a bright clinic"/>
  </svg>
  <p class="eyebrow" style="left:613px;top:138px">We're renovating to serve you better</p>
  <h2 class="heading" style="left:613px;top:160px;width:360px">Exciting things are happening!</h2>
  <p class="body-copy" style="left:613px;top:239px;width:380px">Marlow Care Partners is continually adding and improving our services to provide patients with access to comprehensive care under one roof. Speak with your healthcare provider about how interventional MSK treatments and regenerative therapy can help you today!</p>
</section>

<footer class="site-footer">
  <div class="brand" style="left:106px;top:84px;font-size:20px"><span class="brand-dot"></span>Marlow Care Partners</div>
  <p class="abs" style="left:106px;top:141px;font-size:12.5px;font-weight:300">✉&nbsp; hello@marlowcarepartners.ca</p>
  <h3 class="footer-title" style="left:337px;top:72px">Locations</h3>
  <ul class="footer-list" style="left:337px;top:108px">
    <li>Cedar Point Medical</li><li>Ridgeview Medical</li><li>Brookfield</li><li>Lakeshore</li><li>Valley Women's Clinic</li>
  </ul>
  <h3 class="footer-title" style="left:601px;top:72px">Quick links</h3>
  <ul class="footer-list" style="left:601px;top:107px">
    <li>For Patients</li><li>For Providers</li><li>Careers</li><li>About Us</li>
  </ul>
  <h3 class="footer-title" style="left:831px;top:72px">Book online</h3>
  <ul class="footer-list" style="left:831px;top:108px">
    <li>Cedar Point Medical</li><li>Ridgeview Medical</li><li>Brookfield</li>
  </ul>
  <svg class="abs" style="left:1054px;top:75px" width="40" height="135" aria-label="Social links">
    <rect x="7" y="7" width="26" height="26" transform="rotate(45 20 20)" fill="none" stroke="#3dd1dc" stroke-width="1.5"/>
    <rect x="7" y="51" width="26" height="26" transform="rotate(45 20 64)" fill="#3dd1dc"/>
    <rect x="7" y="95" width="26" height="26" transform="rotate(45 20 108)" fill="none" stroke="#3dd1dc" stroke-width="1.5"/>
  </svg>
</footer>
<div class="footer-bar">©2022 Marlow Care Partners. All Right Reserved<span>I</span>Legal<span>I</span>Privacy Policy</div>

</body>
</html>
```